Company or website name
- Copperfield Staff Bulletins
- Links to the website
- I 'breathe fresh life' into office workplaces with these inspirational wellbeing newsletters! =)
- Other Facts

```html
<!DOCTYPE html>
<html lang="en">
<head>
<meta charset="utf-8">
<title>Copperfield Staff Bulletins – Employee Well Being Program</title>
<link href="https://fonts.googleapis.com/css2?family=Arimo:wght@400;700&family=Caveat:wght@500&family=Gelasio:wght@400&family=Playball&family=Tinos:wght@400&display=swap" rel="stylesheet">
<style>
:root{
  --space-dark:#05060f;
  --aurora:#8a3fd1;
  --title-green:#2fd12a;
  --issue-yellow:#f3e33a;
  --rule-green:#8ccf3a;
  --ink:#1a1a1a;
  --interest-bg:#e8dde2;
  --interest-head:#2a3585;
  --laugh-bg:#fbcfa8;
  --know-head-bg:#fbe9a9;
  --know-head:#2f6a10;
  --know-q:#d9cf9a;
  --know-body-bg:#fde7a5;
  --know-text:#6b1030;
  --swap-bg:#dfe2d6;
  --swap-head:#4a1e6e;
  --yummy-bg:#cccaf6;
  --yummy-orange:#f47214;
  --events-bg:#efefef;
  --events-head:#2b3aa0;
  --events-city:#2b3aa0;
  --clock:#b9b9b9;
  --footer-bg:#000;
}
*{margin:0;padding:0;box-sizing:border-box}
html,body{width:1200px;height:3318px;overflow:hidden;background:#fff}
.page{position:relative;width:1200px;height:3318px;color:var(--ink)}
.section{position:absolute}

.masthead{left:0;top:0;width:1200px;height:264px;overflow:hidden}
.masthead-sky{position:absolute;inset:0;background:
  radial-gradient(ellipse 55% 35% at 60% 42%,rgba(255,255,255,.75),rgba(190,110,255,.35) 45%,transparent 75%),
  radial-gradient(ellipse 70% 45% at 45% 30%,rgba(60,200,120,.45),transparent 70%),
  linear-gradient(180deg,#2a1846 0%,var(--aurora) 35%,#3b1b6c 55%,var(--space-dark) 100%)}
.issue{position:absolute;right:34px;top:18px;font:400 30px 'Arimo',sans-serif;color:var(--issue-yellow);word-spacing:6px}
.masthead-title{position:absolute;left:0;width:1200px;top:76px;text-align:center;font:400 82px 'Playball',cursive;color:#fff;letter-spacing:1px;
  -webkit-text-stroke:2px #222;paint-order:stroke fill}
.masthead-title .accent{color:var(--title-green)}
.rule{left:0;top:264px;width:1200px;height:17px;background:var(--rule-green)}

.intro{left:13px;top:288px;width:1175px;font:400 28px/38px 'Gelasio',serif;color:#111;text-indent:32px}
.intro .drop{font-size:40px}

.interest{left:0;top:534px;width:609px;height:1726px;background:var(--interest-bg);padding:12px 6px 0 7px}
.panel-head{font:400 40px 'Playball',cursive;text-align:center}
.interest .panel-head{color:var(--interest-head);margin-bottom:18px}
.interest p{font:400 19px/24.9px 'Tinos',serif;color:#1d1d1d;margin-bottom:24.9px}
.interest .lead{text-indent:30px}
.interest .drop{font-size:32px}

.laugh{left:0;top:2260px;width:609px;height:287px;background:var(--laugh-bg)}
.laugh-face{position:absolute;left:24px;top:58px;width:210px;height:210px;border-radius:50%;background:radial-gradient(circle at 40% 35%,#fffbd2,#ecdc70 70%,#cdbb3c)}
.laugh h3{position:absolute;left:190px;top:20px;font:400 34px 'Arimo',sans-serif;color:#111}
.laugh p{position:absolute;left:298px;font:400 28px/38px 'Arimo',sans-serif;color:#111;width:300px}

.know-head{left:609px;top:534px;width:591px;height:65px;background:var(--know-head-bg);text-align:center;line-height:62px}
.know-head .q{font:400 44px 'Arimo',sans-serif;color:var(--know-q);letter-spacing:4px;vertical-align:middle}
.know-head .panel-head{display:inline-block;color:var(--know-head);font-size:44px;vertical-align:middle;margin:0 10px}
.know-photo{left:609px;top:599px;width:591px;height:386px;background:radial-gradient(circle at 32% 22%,#fff 0,#cfe4ff 9%,#5f9ddf 30%,#1f5fb4 70%,#164d98 100%)}
.know-body{left:609px;top:985px;width:591px;height:197px;background:var(--know-body-bg);padding:10px 10px 0 15px;font:400 21.5px/27.5px 'Gelasio',serif;color:var(--know-text)}
.know-body .drop{font-size:36px}

.swap{left:609px;top:1182px;width:591px;height:554px;background:var(--swap-bg);padding:14px 14px 0 15px}
.swap-head{display:flex;justify-content:center;align-items:center;gap:14px;margin-bottom:14px}
.swap-head .panel-head{color:var(--swap-head);font-size:54px}
.swap h4{font:400 25px 'Gelasio',serif;margin-bottom:14px;color:#111}
.swap p{font:400 22.5px/30px 'Gelasio',serif;color:#111}
.swap .drop{font-size:40px}

.yummy{left:609px;top:1736px;width:591px;height:811px;background:var(--yummy-bg);padding:10px 0 0 15px;font-family:'Arimo',sans-serif;color:#111}
.yummy h2{text-align:center;font:700 44px 'Arimo',sans-serif;color:var(--yummy-orange);margin-bottom:16px;padding-right:15px}
.yummy h3{font:400 32px 'Arimo',sans-serif;margin-bottom:8px}
.yummy h5{font:400 21px 'Arimo',sans-serif;margin-bottom:28px}
.ingredients{list-style:none;font:400 21px/27.5px 'Arimo',sans-serif;margin-bottom:30px}
.method{list-style:none;font:400 21px/27.5px 'Arimo',sans-serif;padding-right:4px}
.yummy-photo{position:absolute;left:271px;top:243px;width:308px;height:229px;background:radial-gradient(circle at 50% 35%,#e85a3a 0,#f2b34a 20%,#88b847 34%,#f6e9e1 55%,#fbf7f4 100%)}

.events{left:0;top:2547px;width:1200px;height:694px;background:var(--events-bg);padding:0 12px}
.events-head{display:flex;align-items:center;justify-content:center;gap:10px;padding-top:32px;margin-bottom:70px}
.events-head h2{font:400 51px 'Tinos',serif;color:var(--events-head);margin:0 14px}
.events p{font:400 23px/32px 'Tinos',serif;color:#111;margin-bottom:33px}
.events .city{color:var(--events-city)}

.footer{left:0;top:3241px;width:1200px;height:77px;background:var(--footer-bg);color:#fff;text-align:center;font:500 44px/77px 'Caveat',cursive}
</style>
</head>
<body>
<main class="page">

  <header class="section masthead">
    <div class="masthead-sky" role="img" aria-label="Night sky with a glowing purple and green aurora"></div>
    <div class="issue">Issue: 12 2009</div>
    <h1 class="masthead-title">Employee <span class="accent">Well Being</span> Program</h1>
  </header>
  <div class="section rule"></div>

  <p class="section intro"><span class="drop">S</span>o much for 'winding down for the year' the silly season can be the most stressful of them all! For maximum wellbeing returns on minimum time investment, look no further than simple breathing. Take a deep breathe in, and then release it - along with any muscle tightness and stress. There you go, make breathing the gift to yourself to turn the silly season into the settled season.</p>

  <article class="section interest">
    <h2 class="panel-head">That’s Interesting....</h2>
    <p class="lead"><span class="drop">H</span>ave you noticed some people seem to be able to eat what they like and still stay slim? Instead of secretly hating them, there are things we can learn about their habits and attitudes that allow them to stay lean. Here are the top 5 nutrition habits of naturally slim people:</p>
    <p>1. They only eat when truly hungry. There are so many cues around us to eat when we are not even physically hungry – we grab a few lollies while we’re at the desk, we have a biscuit from the kitchen with our morning tea, we eat a slice of cake because it’s a colleagues’ birthday...the list is endless! Unfortunately, this non-hungry snacking really does add up. Naturally slim people eat when they are truly physically hungry, and not because they are bored, frustrated, celebrating, with a group of people, stressed or because ‘it’s time to eat’. They listen to their own body and hunger rather than watching the clock, eating because other people expect them to, or eating because ‘it’s there’.</p>
    <p>2. Naturally slim and healthy people listen to their bodies. Some days we are hungrier than others, some days we crave different things. The body has its own innate wisdom, and some days our bodies require more fuel. Instead of dieting (trying to control or deny natural hunger,) naturally slim people honour their hunger and nurture their bodies. Our bodies know exactly what is needed at any given moment, and when we tune in we’re naturally led to the perfect foods for us.</p>
    <p>3. They enjoy a drink - and no, we are not talking about alcohol! Naturally slim people drink lots of water and stay well hydrated. They don’t confuse thirst with hunger. Most times when we think we are hungry, we are really thirsty, and our first response to this feeling should be to have a glass of water.</p>
    <p>4. Healthy people don’t do fad diets. Instead they eat in moderation, focus on nutrition and they don’t really think about food unless they are physically hungry. Some days they eat more, some days they eat less, all depending on what their body needs. Dieting is denying yourself, and truly healthy people, inside and out, would never deny themselves. Instead they honour and nourish their bodies with the best quality food. Which leads to the final point...</p>
    <p>5. Naturally slim and healthy people get pleasure for example, when they eat a salad they think of all the vitamins, minerals and nutrients that they are providing their body and they feel good taking care of themselves. They don’t see a salad as deprivation at all, instead they feel nourished. Naturally slim people see food as fuel. They seek out the highest quality fuel, and gain pleasure nourishing each cell with the best quality nutrients.</p>
    <p class="lead">When it comes down to it, no one is “naturally” slim at all. We all have the choice of abusing and destroying our bodies, or nurturing and creating health. It all lies in our approach and thoughts and behaviours – that’s what creates our reality in all areas of life. Our body is always a reflection of what’s going on inside, and when we have positive thoughts and a healthy attitude towards food, we’re naturally guided to the best fuel to nourish ourselves and keep us at our perfect weight.</p>
  </article>

  <aside class="section laugh">
    <div class="laugh-face" role="img" aria-label="Round yellow smiley character"></div>
    <h3>Ha! Ha! Ha!</h3>
    <p style="top:82px">“Waiter! This coffee tastes like mud.”</p>
    <p style="top:192px">“Yes sir, it’s fresh ground.”</p>
  </aside>

  <div class="section know-head"><span class="q">??</span><h2 class="panel-head">Did You Know?</h2><span class="q">??</span></div>
  <div class="section know-photo" role="img" aria-label="Woman silhouetted against a bright blue sky, drinking from a water bottle in the sun"></div>
  <p class="section know-body"><span class="drop">T</span>he human body is comprised of 80% water and a mere 2% loss in body water can reduce your energy levels by 20 per cent! The effects of dehydration are poor concentration, tiredness and headaches, and you simply can’t think as efficiently when you are dehydrated. So drink up !</p>

  <section class="section swap">
    <div class="swap-head">
      <svg width="40" height="40" viewBox="0 0 40 40" aria-hidden="true"><path d="M34 30 C30 14 20 10 10 12" fill="none" stroke="#111" stroke-width="4"/><path d="M4 12 L14 4 L14 20 Z" fill="#111"/></svg>
      <h2 class="panel-head">Swap This!</h2>
      <svg width="40" height="40" viewBox="0 0 40 40" aria-hidden="true"><path d="M8 6 C12 22 22 26 30 26" fill="none" stroke="#111" stroke-width="4"/><path d="M36 26 L26 34 L26 18 Z" fill="#111"/></svg>
    </div>
    <h4>Coffee for green tea:</h4>
    <p><span class="drop">A</span> skim latte has around 100-200 calories, and is a hit of false energy. Caffeine can enervate your body, and in the long term it leaves you fatigued. Herbal teas have only 5 calories, and each has their own natural benefits for your body. Green tea does have some caffeine (around 1/3 of the amount in coffee) but is also a powerful anti-oxidant, chamomile has calming properties, ginger root is excellent for improving circulation and peppermint tea aids digestion and is good for stress relief.</p>
  </section>

  <section class="section yummy">
    <h2>Yummy!</h2>
    <h3>Tasty Tuscan Chicken</h3>
    <h5>INGREDIENTS:</h5>
    <ul class="ingredients">
      <li>- 1 Punnet grape tomatoes</li>
      <li>- 1/2 cup (50g) pimento stuffed green olives</li>
      <li>- 2 tbs olive oil</li>
      <li>- Juice of 1/2 lemon</li>
      <li>- 2 Chicken breast fillets</li>
      <li>- 1 tbs capers</li>
      <li>- ½ cup</li>
      <li>- Rice</li>
      <li>- Basil leaves</li>
      <li>- Brown rice</li>
      <li>- Green salad to serve</li>
    </ul>
    <div class="yummy-photo" role="img" aria-label="Cupped hands holding a mix of fresh fruit"></div>
    <h5 style="margin-bottom:18px">METHOD:</h5>
    <ol class="method">
      <li>1. Preheat oven to 180°C. Combine tomatoes, olives, capers, olive oil and lemon juice in a bowl.</li>
      <li>2. Season chicken to taste and fry in a non stick pan for 3 minutes each side, until golden brown. Transfer to a baking pan.</li>
      <li>3. Pour the tomato mixture over the chicken in the baking pan and season to taste. Bake for 15 minutes.</li>
      <li>4. Top with a few basil leaves and serve with brown rice and leaves.</li>
    </ol>
  </section>

  <section class="section events">
    <div class="events-head">
      <svg width="290" height="90" viewBox="0 0 290 90" aria-hidden="true" fill="none" stroke="var(--clock)" stroke-width="4" stroke-linecap="round">
        <circle cx="45" cy="45" r="40"/><path d="M45 45 L20 38 M45 45 L28 56"/>
        <circle cx="145" cy="45" r="40"/><path d="M145 45 L145 18 M145 45 L128 52"/>
        <circle cx="245" cy="45" r="40"/><path d="M245 45 L232 24 M245 45 L266 32"/>
      </svg>
      <h2>What’s on this weekend?</h2>
      <svg width="290" height="90" viewBox="0 0 290 90" aria-hidden="true" fill="none" stroke="var(--clock)" stroke-width="4" stroke-linecap="round">
        <circle cx="45" cy="45" r="40"/><path d="M45 45 L24 34 M45 45 L54 70"/>
        <circle cx="145" cy="45" r="40"/><path d="M145 45 L145 70 M145 45 L160 28"/>
        <circle cx="245" cy="45" r="40"/><path d="M245 45 L268 32 M245 45 L232 50"/>
      </svg>
    </div>
    <p><span class="city">Sydney 28th-</span> Harbourside Quay Christmas Concert A family concert with performances from The Pyjama Twins. Convention Centre Forecourt, Harbourside Quay from 8pm, free.</p>
    <p><span class="city">Melbourne 28th and 29th-</span> Urban Dash Challenge The exciting physical and mental urban adventure challenge is back on 28-29 November when teams of three will run, ride, kayak, climb and abseil across a course that’s only revealed to them hours before they begin. For more information call 1800 555 019.</p>
    <p><span class="city">Canberra 28 &amp; 29th-</span> Ridgeview Festival On Saturday 28 November, the Big 21st Birthday Bash Street Party will be held in Marlow Street. On Sunday 29 November, The Ridgeview Festival will celebrate 21 years with a free festival featuring live music, a children’s show, skateboarding and rollerblading, fireworks, market stalls and more in Ridgeview Town Park.</p>
    <p><span class="city">Brisbane 28 &amp; 29-</span> Santa Celebration Activities include a jumping castle, a train simulator, art and craft, a screening of the Northbound Sleigh and more. There will also be a visit from Santa. Activities are free after general museum entry. The Railyard Heritage Museum, Depot St, Westvale.</p>
  </section>

  <footer class="section footer">"There are no shortcuts to any place worth going" - Marian Holt</footer>

</main>
</body>
</html>
```